Winter Soccer Training

Youth Soccer Academy, I want to advertise Winter Training $195.00(Includes training for one month, Uniform) after first Month $145 per month.

Target Market(s)

kids from 5 years to 18

Industry/Entity Type

Training

Colors
3176b5

Requirements
Must have
• Winter Training
• Location: Harbor Fieldhouse
• 4827 Maple Crest rd Brookvale MD 20999
• Phone:(240)555-0187
• Training Schedule
• Tuesday and Thursday
• 5:30pm to 6:30pm 5 to 10 years old
• 6:30pm to 7:30pm 11 to 15 years old
• 7:30pm to 8:30pm 16 to 19 years old
• www.velantoacademy.example
Nice to have
• Soccer Field
Should not have
• Soccer Balls

```html
<!DOCTYPE html>
<html lang="en">
<head>
<meta charset="utf-8">
<title>Velanto Soccer Academy – Winter Training</title>
<link href="https://fonts.googleapis.com/css2?family=Righteous&family=Open+Sans:wght@600;700;800&family=Roboto:wght@400;500&display=swap" rel="stylesheet">
<style>
  :root{
    --stage:#7a9bb9;
    --brand:#3176b5;
    --navy:#06204a;
    --deep:#0a3672;
    --cyan:#1fc6f0;
    --sky:#5fd5f5;
    --white:#ffffff;
    --pale:#cfe4f7;
    --card-light:#d9e8f7;
  }
  *{box-sizing:border-box;margin:0;padding:0}
  html,body{width:1200px;height:696px;overflow:hidden}
  body{background:var(--stage);position:relative;font-family:"Open Sans",sans-serif}

  /* ---------- back of card ---------- */
  .card-back{
    position:absolute;left:110px;top:38px;width:440px;height:620px;
    background:linear-gradient(180deg,var(--card-light) 0%,#7fa9d6 45%,var(--brand) 80%,#1f5592 100%);
  }
  .stamp-box{position:absolute;right:40px;top:40px;width:80px;height:64px;border:1.5px solid var(--deep)}
  .address-lines{position:absolute;right:40px;top:150px;width:230px}
  .address-lines span{display:block;height:1.5px;background:var(--deep);margin-bottom:30px}
  .back-brand{
    position:absolute;right:36px;bottom:48px;display:flex;align-items:center;gap:10px;
    font-weight:800;font-size:17px;color:var(--white);line-height:1.15;
  }
  .brand-dot{width:18px;height:18px;border-radius:50%;background:var(--white);flex:none}

  /* ---------- front of card ---------- */
  .card-front{
    position:absolute;left:650px;top:38px;width:440px;height:620px;overflow:hidden;
    background:linear-gradient(180deg,#0b4c96 0%,#0a3a7a 40%,var(--navy) 85%,#031634 100%);
    color:var(--white);
  }
  .header-art{
    position:absolute;left:0;top:0;width:100%;height:190px;
    background:radial-gradient(ellipse at 75% 35%,var(--sky) 0%,var(--cyan) 25%,#1683c9 55%,#0b4c96 100%);
  }
  .field-art{
    position:absolute;left:0;top:190px;width:100%;height:340px;
    background:radial-gradient(ellipse at 50% 30%,rgba(40,140,220,.55) 0%,rgba(10,60,130,0) 70%);
  }
  .swoosh{position:absolute;left:0;top:130px;width:440px;height:90px}
  .front-brand{
    position:absolute;left:24px;top:50px;display:flex;align-items:center;gap:8px;
    font-weight:800;font-size:16px;line-height:1.15;color:var(--white);width:150px;
  }
  .title{position:absolute;right:22px;top:24px;text-align:center;font-family:"Righteous",sans-serif;font-weight:400;color:var(--white);line-height:.9}
  .title .small{display:block;font-size:30px}
  .title .big{display:block;font-size:62px}
  .title .sub{display:block;font-size:30px}

  .offer{position:absolute;left:24px;top:232px;width:392px;height:62px}
  .offer-pill{
    position:absolute;inset:0;border-radius:31px;background:var(--deep);
    border:4px solid var(--pale);box-shadow:0 3px 6px rgba(0,0,0,.4);
  }
  .offer-label{position:absolute;left:26px;top:12px;font-weight:800;font-size:15px;line-height:1.1;text-align:center}
  .offer-bubble{position:absolute;left:112px;top:-16px;width:112px;height:96px}
  .offer-price{position:absolute;left:112px;top:5px;width:112px;text-align:center;font-weight:800;font-size:28px;line-height:38px;color:var(--white)}
  .offer-price sup{font-size:14px;vertical-align:10px}
  .offer-note{position:absolute;left:236px;top:12px;font-weight:700;font-size:12.5px;line-height:1.35}

  .after{position:absolute;left:0;top:318px;width:100%;text-align:center;font-weight:700;font-size:19px}

  .schedule-tag{
    position:absolute;left:50%;top:360px;transform:translateX(-50%);
    padding:5px 18px;background:linear-gradient(180deg,#2f86cf,#15559f);border:2px solid var(--pale);
    font-weight:700;font-size:14px;white-space:nowrap;
  }
  .days{position:absolute;left:0;top:398px;width:100%;text-align:center;font-weight:800;font-size:17px}
  .days::before,.days::after{content:"";position:absolute;top:12px;width:70px;height:2px;background:var(--pale)}
  .days::before{left:24px}
  .days::after{right:24px}

  .slots{position:absolute;left:34px;top:430px;width:372px;list-style:none}
  .slots li{
    height:36px;margin-bottom:9px;display:flex;align-items:center;justify-content:center;
    background:linear-gradient(180deg,#2f86cf,#0f4c96);border:2px solid var(--pale);border-radius:3px;
    box-shadow:0 2px 4px rgba(0,0,0,.45);font-family:"Roboto",sans-serif;font-size:19px;
  }

  .contact{position:absolute;left:0;top:578px;width:100%;text-align:center;font-weight:600;font-size:10px}
  .location-band{
    position:absolute;left:0;bottom:0;width:100%;height:22px;background:var(--brand);
    font-weight:700;font-size:10.5px;display:flex;align-items:center;padding-left:14px;
  }
</style>
</head>
<body>

<section class="card-back" aria-label="Back of card">
  <div class="stamp-box"></div>
  <div class="address-lines"><span></span><span></span><span></span><span></span></div>
  <div class="back-brand"><span class="brand-dot"></span><span>Velanto<br>Soccer Academy</span></div>
</section>

<section class="card-front" aria-label="Front of card">
  <div class="header-art" role="img" aria-label="Abstract light-blue sports motion pattern"></div>
  <div class="field-art" role="img" aria-label="Soft blue abstract field backdrop"></div>
  <svg class="swoosh" viewBox="0 0 440 90" aria-hidden="true">
    <path d="M0 80 Q200 20 440 50 L440 64 Q210 36 0 90 Z" fill="#ffffff"/>
    <path d="M0 90 Q210 36 440 64 L440 72 Q220 48 0 90 Z" fill="#8fc7ef"/>
  </svg>

  <div class="front-brand"><span class="brand-dot"></span><span>Velanto<br>Soccer Academy</span></div>

  <h1 class="title">
    <span class="small">Youth</span>
    <span class="big">Soccer</span>
    <span class="sub">Academy</span>
  </h1>

  <div class="offer">
    <div class="offer-pill"></div>
    <div class="offer-label">Winter<br>Training</div>
    <svg class="offer-bubble" viewBox="0 0 112 96" aria-hidden="true">
      <polygon points="30,66 18,94 50,74" fill="#ffffff"/>
      <ellipse cx="56" cy="40" rx="48" ry="38" fill="#ffffff"/>
      <ellipse cx="56" cy="40" rx="42" ry="32" fill="#0a3672"/>
    </svg>
    <div class="offer-price"><sup>$</sup>195</div>
    <div class="offer-note">Includes training for<br>One Month + Uniform</div>
  </div>

  <p class="after">after first Month $145 per month</p>

  <div class="schedule-tag">Training Schedule</div>
  <p class="days">Tuesday and Thursday</p>

  <ul class="slots">
    <li>5:30pm to 6:30pm 5 to 10 years old</li>
    <li>6:30pm to 7:30pm 11 to 15 years old</li>
    <li>7:30pm to 8:30pm 16 to 19 years old</li>
  </ul>

  <p class="contact">Phone : (240)555-0187 &nbsp; Web: www.velantoacademy.example</p>
  <div class="location-band">Harbor Fieldhouse, 4827 Maple Crest rd Brookvale MD 20999</div>
</section>

</body>
</html>
```